business card with logo Marigold Nails & Spa 2815 SW Harlow Ave Portland OR 97099

Would like to have a business card with our logo.
like bottle of polish with our logo or letter M on it
want something that first glance would let you know that it is a nail salon.
like the hands with polish bottle dripping.
like black or White back ground

Marigold Nails & Spa
(The Velvet Retreat)
2815 SW Harlow Ave
Portland, OR 97099
Call or Text: 1-555-714-3928
www.MarigoldNailsnSpa.example
Open 7 days a week.
After 7:00 PM is by appointment only.
Closed only on Thanksgiving & Christmas.

Target Market(s)

20%Man and 80%Woman 13-70

Industry/Entity Type

Business

Contact Information for Business Card

Elegant with Logo-Business name- address-phone-open days. closed day.

Font styles to use
Decorative
Script

Colors
000000

Requirements
Must have
• Logo and place for Technician Name
• Marigold Nails & Spa
• (The Velvet Retreat)
• 2815 SW Harlow Ave
• Portland, OR 97099
• Call or Text: 1-555-714-3928
• Open 7 days a week
• Closed only on Thanksgiving & Christmas.
• We accepted all major credit cards but prefer cash. Thank you
Nice to have
• Nail polish bottle with our Logo or letter M
Should not have
• too colorful

```html
<!DOCTYPE html>
<html lang="en">
<head>
<meta charset="utf-8">
<title>Marigold Nails &amp; Spa – Business Card</title>
<link href="https://fonts.googleapis.com/css2?family=Arimo:wght@400;700&family=Pinyon+Script&display=swap" rel="stylesheet">
<style>
  :root {
    --ink: #111111;
    --ink-soft: #3a3a3a;
    --paper: #ffffff;
    --backdrop: #e9e7e4;
    --mist: #d4d4d4;
    --accent: #8dc63f;
    --bottle-light: #f4f4f4;
    --bottle-shade: #c9c9c9;
  }
  * { box-sizing: border-box; margin: 0; padding: 0; }
  html, body { width: 1200px; height: 800px; overflow: hidden; }
  body {
    background: var(--backdrop);
    display: flex; align-items: center; justify-content: center;
    font-family: "Arimo", Arial, sans-serif;
    color: var(--ink);
  }
  .card {
    position: relative;
    width: 420px; height: 735px;
    background: var(--paper);
    box-shadow: 0 10px 30px rgba(0,0,0,.15);
    overflow: hidden;
  }
  .watercolor-wash {
    position: absolute; left: 150px; top: 180px; width: 300px; height: 420px;
    background: radial-gradient(ellipse at 55% 40%, rgba(190,190,190,.55), rgba(220,220,220,.25) 45%, rgba(255,255,255,0) 72%);
  }
  .brand {
    position: absolute; left: 40px; top: 50px; right: 40px;
    text-align: center;
  }
  .brand-name {
    font-weight: 700; font-size: 62px; letter-spacing: -1px; line-height: 1;
    display: inline-flex; align-items: center; gap: 12px;
  }
  .brand-dot { width: 14px; height: 14px; border-radius: 50%; background: var(--accent); }
  .brand-sub { font-weight: 700; font-size: 30px; line-height: 1.2; }
  .brand-tagline { font-size: 15px; letter-spacing: 2px; margin-top: 6px; color: var(--ink-soft); }

  .polish-bottle {
    position: absolute; left: 34px; top: 262px; width: 120px; height: 190px;
    border-radius: 10px;
    background: linear-gradient(90deg, var(--bottle-shade), var(--bottle-light) 45%, var(--bottle-shade));
  }
  .details {
    position: absolute; right: 34px; top: 268px; width: 240px;
    text-align: right;
  }
  .tech-name { font-weight: 700; font-size: 26px; }
  .tech-role { font-family: "Pinyon Script", cursive; font-size: 20px; color: var(--ink-soft); }
  .call-label { font-size: 17px; color: var(--ink-soft); margin-top: 2px; }
  .phone { font-size: 30px; letter-spacing: -.5px; margin-top: 2px; }

  .info {
    position: absolute; right: 34px; left: 34px; top: 470px;
    text-align: right; line-height: 1.4;
  }
  .shop { font-size: 17px; }
  .address { font-size: 14px; color: var(--ink-soft); }
  .hours { font-size: 16px; margin-top: 6px; }
  .payment { margin-top: 10px; display: flex; justify-content: flex-end; align-items: center; gap: 5px; }
  .pay-card { width: 26px; height: 17px; border-radius: 2px; background: var(--mist); }
  .pay-note { font-size: 15px; }
  .pay-note strong { font-size: 17px; }
  .thanks { font-size: 15px; color: var(--ink-soft); }
  .website {
    position: absolute; left: 0; right: 0; bottom: 26px; text-align: center;
    font-family: "Pinyon Script", cursive; font-size: 19px; letter-spacing: 3px;
  }
</style>
</head>
<body>
  <article class="card">
    <div class="watercolor-wash" role="img" aria-label="Soft grey watercolor splash"></div>

    <header class="brand">
      <div class="brand-name"><span>Marigold</span><span class="brand-dot"></span></div>
      <div class="brand-sub">Nails n Spa</div>
      <div class="brand-tagline">(The Velvet Retreat)</div>
    </header>

    <div class="polish-bottle" role="img" aria-label="White nail polish bottle bearing the salon name"></div>

    <section class="details">
      <div class="tech-name">Lena Hart</div>
      <div class="tech-role">Nail Technician</div>
      <div class="call-label">Call / Text</div>
      <div class="phone">1-555-714-3928</div>
    </section>

    <section class="info">
      <div class="shop">Marigold Nails &amp; Spa</div>
      <div class="address">2815 SW Harlow Ave Portland, OR 97099</div>
      <div class="hours">Open <strong>7 days a week</strong><br>
        After 7:00 PM is <strong>by appointment only</strong><br>
        <strong>Closed</strong> only on <strong>Thanksgiving &amp; Christmas</strong></div>
      <div class="payment">
        <span class="pay-card"></span><span class="pay-card"></span><span class="pay-card"></span><span class="pay-card"></span>
      </div>
      <div class="pay-note">Credit Cards accepted but <strong>prefer CASH</strong></div>
      <div class="thanks">Thank you</div>
    </section>

    <footer class="website">www.MarigoldNailsnSpa.example</footer>
  </article>
</body>
</html>
```